Web and Logo Design for eCommerce site

We're launching a sister brand and require a full design for the site.

The site must have an established feel and appeal to corporate and institutional buyers.
Updates

Just a note about the wireframe design:

The Search & Rescue / Coast Guard / NVTB, etc. in the header area aren't buttons or menu items, but rather just info (along the lines of a tagline).  Sort of a "who we serve" sort of thing.

Worth noting is that it's specifically geared towards LARGE BUYERS.  For example, a police force buying 200 headlamps and 85 pairs of gloves.  So they'll register + sign in and then add a bunch of items to a RFQ.

Aim for a professional, masculine design.

Target Market(s)

We will be selling outdoor gear to the military, law enforcement, fire and rescue and first responders.

Requirements
Must have
• We require:
- Logo (vector based)

Site:
- template page
* main site template, re-skinned version of our current site
* horizontal drop-down menu
- product listings page
* thumbnail view of products
- product details page
* including elements such as product image, color/size selector, descriptions and specs (again, based loosely on our current website)
- account management page
* illustrating basic data entry styles for text box, buttons, grid, etc.

The site needs to be given a responsive design, so 2 versions of each design should be presented for desktop + mobile views.

Additional funds are available if the designer is able to fully implement the designs into a responsive framework such as bootstrap.

Nice to have
• Clean, professional design similar to:

http://military.brambletrekgear.com/gov/accessories/gloves.html

http://leaf.quenvolt.com/ProductFind.aspx?language=EN&category=Hardshell&subcat=Waterproof_Jackets

```html
<!DOCTYPE html>
<html lang="en">
<head>
<meta charset="utf-8">
<title>Tundrax Field Pro Supply</title>
<link href="https://fonts.googleapis.com/css2?family=Bebas+Neue&family=Arimo:wght@400&display=swap" rel="stylesheet">
<style>
  :root {
    --bg: #2c2c2c;
    --bg-dark: #232323;
    --band: #050505;
    --band-text: #5b5757;
    --white: #ffffff;
    --btn-top: #3a3a3a;
    --btn-bottom: #141414;
    --btn-edge: #6a6a6a;
    --nav-active-top: #6b6b6b;
    --nav-active-bottom: #3e3e3e;
    --hero-a: #6f6a55;
    --hero-b: #3e3a2e;
    --hero-c: #8a8466;
    --arrow: #1a1a1a;
    --arrow-edge: #7a7a7a;
  }
  * { margin: 0; padding: 0; box-sizing: border-box; }
  html, body { width: 1200px; height: 725px; overflow: hidden; }
  body {
    position: relative;
    background: radial-gradient(ellipse at 50% 40%, #303030 0%, var(--bg) 55%, var(--bg-dark) 100%);
    font-family: "Arimo", Arial, sans-serif;
    color: var(--white);
  }
  .brand {
    position: absolute; left: 250px; top: 48px; width: 120px;
    display: flex; align-items: center; gap: 8px;
  }
  .brand-mark { flex: none; width: 12px; height: 12px; background: var(--white); }
  .brand-name {
    font-family: "Bebas Neue", sans-serif; font-weight: 400;
    font-size: 32px; line-height: 30px; letter-spacing: 1px; color: var(--white);
  }
  .site-title {
    position: absolute; left: 380px; top: 82px;
    font-family: "Bebas Neue", sans-serif; font-weight: 400;
    font-size: 41px; letter-spacing: 0.5px; line-height: 1; white-space: nowrap;
  }
  .tagline {
    position: absolute; left: 660px; top: 11px; width: 320px;
    font-family: "Bebas Neue", sans-serif; font-size: 29px; line-height: 25px; text-align: center;
  }
  .btn {
    position: absolute; display: flex; align-items: center; justify-content: center;
    font-family: "Bebas Neue", sans-serif; color: var(--white); letter-spacing: 1px;
    background: linear-gradient(var(--btn-top), var(--btn-bottom));
    border: 2px solid var(--btn-edge);
    box-shadow: 0 0 0 2px #111, 0 3px 6px rgba(0,0,0,.6);
  }
  .btn-login { left: 818px; top: 111px; width: 146px; height: 41px; font-size: 29px; }
  .btn-register { left: 527px; top: 579px; width: 146px; height: 39px; font-size: 29px; }
  .audience-band {
    position: absolute; left: 0; top: 158px; width: 1200px; height: 32px;
    background: var(--band);
    font-family: "Bebas Neue", sans-serif; font-size: 26px; color: var(--band-text);
    text-align: center; line-height: 34px; letter-spacing: 0.5px; word-spacing: 2px;
  }
  .main-nav { position: absolute; left: 0; top: 190px; width: 1200px; height: 34px; }
  .main-nav a {
    position: absolute; top: 0; height: 34px;
    display: flex; align-items: center; justify-content: center;
    color: var(--white); text-decoration: none; font-size: 13px; line-height: 13px;
    text-align: center; white-space: nowrap;
  }
  .main-nav .is-active {
    width: 94px;
    background: linear-gradient(var(--nav-active-top), var(--nav-active-bottom));
    border: 1px solid #8a8a8a;
  }
  .nav-rescue { left: 260px; }
  .nav-footwear { left: 379px; }
  .nav-clothing { left: 469px; }
  .nav-tents { left: 547px; }
  .nav-camping { left: 661px; }
  .nav-snow { left: 781px; }
  .nav-brands { left: 892px; }
  .hero {
    position: absolute; left: 360px; top: 279px; width: 480px; height: 282px;
    border: 1px solid #555; box-shadow: 0 4px 12px rgba(0,0,0,.7);
  }
  .hero-photo {
    position: absolute; inset: 0;
    background: radial-gradient(ellipse at 45% 40%, var(--hero-c) 0%, var(--hero-a) 35%, var(--hero-b) 80%, #262420 100%);
  }
  .hero-shade { position: absolute; inset: 0; background: rgba(0,0,0,.35); }
  .hero-text {
    position: relative; padding-top: 33px;
    font-family: "Bebas Neue", sans-serif; font-size: 31px; line-height: 37.5px;
    text-align: center; letter-spacing: 1.3px;
    text-shadow: 0 1px 3px rgba(0,0,0,.8);
  }
  .connectors { position: absolute; left: 455px; top: 560px; }
</style>
</head>
<body>
  <div class="brand">
    <span class="brand-mark"></span>
    <span class="brand-name">Tundrax<br>.ca</span>
  </div>
  <h1 class="site-title">Tundrax Field Pro Supply</h1>
  <p class="tagline">"Great Outfoor Gear for<br>Canada's First Responders"</p>
  <a class="btn btn-login">Login</a>

  <div class="audience-band">Search&amp;Rescue ** CoastGuard ** NVTB ** Fire ** Military ** LawEnforcement</div>

  <nav class="main-nav">
    <a class="nav-rescue is-active">Rescue Gear</a>
    <a class="nav-footwear">Footwear</a>
    <a class="nav-clothing">Clothing</a>
    <a class="nav-tents">Tents, Mats<br>Sleeping Bags</a>
    <a class="nav-camping">Camping Gear</a>
    <a class="nav-snow">Snow Sports</a>
    <a class="nav-brands">Brands</a>
  </nav>

  <section class="hero">
    <div class="hero-photo" role="img" aria-label="Photo of a soldier in field gear beside a helicopter on a grassy slope"></div>
    <div class="hero-shade"></div>
    <p class="hero-text">Please register to enter and enjoy<br>Canada's best selection of aoutdoor<br>gear at special pricing and terms<br>that reflect you commitment to<br>service and duty, your unique<br>position and credentials.</p>
  </section>

  <svg class="connectors" width="290" height="60" viewBox="0 0 290 60" aria-hidden="true">
    <g fill="var(--arrow)" stroke="var(--arrow-edge)" stroke-width="1.5">
      <path d="M5 0 H19 V32 H50 V22 L70 39 L50 56 V46 H5 Z"/>
      <path d="M285 0 H271 V32 H240 V22 L220 39 L240 56 V46 H285 Z"/>
    </g>
  </svg>
  <a class="btn btn-register">Register</a>
</body>
</html>
```